Business Card design for consulting company

We are a small consulting company (Valmor Consulting) just starting out and need a business card design with a simple yet slick logo. We provide client focused consultancy support to manage and advise on procurement and acquisition projects for private businesses. Most of our projects are conducted for large well established companies and involve a fair degree of international work, so we would like to reflect that in the design. A large part of the business is also understanding client needs and then connecting them to, or sourcing the right solutions. So we would like to communicate our professionalism, an international focus and our willingness to provide tailored client solutions.

Target Market(s)

Generally we deal with middle to senior executive levels at large companies or with some high wealth private clients/companies. Mostly a conservative group so we want to project a sharp, professional and international image.

Industry/Entity Type

Consulting

Requirements
Must have
• Looking for a simple double sided business card design. Need to have our business name (Valmor Consulting), a person''s name and position title, and our company contact details. Also need a logo that would also convey the international nature of our consultancy.

```html
<!DOCTYPE html>
<html lang="en">
<head>
<meta charset="utf-8">
<title>Valmor Consulting – Business Card</title>
<link rel="stylesheet" href="https://fonts.googleapis.com/css2?family=Roboto:wght@300;400;500&family=Roboto+Condensed:wght@400;500&family=Arial+Narrow&display=swap">
<style>
  :root {
    --page-bg: #ffffff;
    --card-front: #ffffff;
    --card-border: #a9adb0;
    --metallic-blue: #4e6f80;
    --ink-black: #1e1e1e;
    --ink-grey: #4f5456;
    --ink-light: #a3a8ab;
    --logo-tint: #9fb8c6;
    --on-blue: #ffffff;
  }
  * { box-sizing: border-box; margin: 0; padding: 0; }
  html, body {
    width: 1200px; height: 1200px; overflow: hidden;
    background: var(--page-bg);
    font-family: "Roboto", Helvetica, Arial, sans-serif;
    font-weight: 300;
  }
  .sheet { position: relative; width: 1200px; height: 1200px; }

  .card {
    position: absolute; left: 296px; width: 576px; height: 312px;
    border-radius: 24px;
  }
  .card--front {
    top: 101px; background: var(--card-front);
    border: 1.5px solid var(--card-border);
  }
  .card--back { top: 493px; background: var(--metallic-blue); }

  /* front */
  .brand {
    position: absolute; top: 40px; right: 27px;
    display: flex; align-items: center; gap: 14px;
  }
  .brand__dot {
    width: 38px; height: 38px; border-radius: 50%;
    border: 2px solid var(--logo-tint);
  }
  .brand__name {
    font-size: 28px; font-weight: 300; color: var(--ink-grey);
    letter-spacing: 0.2px;
  }
  .person {
    position: absolute; left: 33px; top: 107px;
    font-size: 18px; color: var(--ink-black); font-weight: 400;
  }
  .person__title {
    font-family: "Roboto Condensed", "Arial Narrow", sans-serif;
    font-weight: 500; font-size: 16px; color: var(--ink-light);
    margin-left: 6px;
  }
  .contacts {
    position: absolute; left: 33px; top: 172px;
    display: grid; grid-template-columns: 178px auto;
    row-gap: 5px; font-size: 14px; color: var(--ink-grey);
  }
  .contact__label {
    display: inline-block; width: 18px;
    font-weight: 500; color: var(--ink-light);
  }
  .contact__label--wide { width: 23px; }
  .address {
    position: absolute; left: 33px; top: 258px;
    font-size: 14px; color: var(--ink-grey);
  }

  /* back */
  .back-brand {
    position: absolute; left: 26px; top: 24px;
    font-size: 26px; font-weight: 300; color: var(--on-blue);
  }
  .website {
    position: absolute; left: 363px; top: 149px;
    font-size: 17px; font-weight: 300; color: var(--on-blue);
  }

  /* print spec */
  .spec {
    position: absolute; left: 403px; top: 922px;
    font-family: Arial, Helvetica, sans-serif; font-weight: 400;
    font-size: 17px; line-height: 22px; color: var(--ink-black);
  }
  .spec p + p { margin-top: 22px; }
  .spec__gap { display: inline-block; width: 18px; }
</style>
</head>
<body>
<main class="sheet">

  <section class="card card--front" aria-label="Card front">
    <div class="brand">
      <span class="brand__dot" aria-hidden="true"></span>
      <span class="brand__name">Valmor Consulting</span>
    </div>

    <p class="person">Daniel Harcourt<span class="person__title">Account Director</span></p>

    <div class="contacts">
      <span><span class="contact__label">t</span>+61 &nbsp;(0)198 765 432</span>
      <span><span class="contact__label contact__label--wide">m</span>+61 &nbsp;(0)198 765 432</span>
      <span><span class="contact__label">f</span>+61 &nbsp;(0)198 765 432</span>
      <span><span class="contact__label contact__label--wide">e</span>dharcourt@valmorconsulting.com.au</span>
    </div>

    <p class="address">2051 - 410 Harbourside Road, &nbsp;Ryde NSW &nbsp;2112 Australia</p>
  </section>

  <section class="card card--back" aria-label="Card back">
    <p class="back-brand">Valmor Consulting</p>
    <p class="website">valmorconsulting.com.au</p>
  </section>

  <div class="spec">
    <p>front:<br>2 color<span class="spec__gap"></span>dark silver blue metallic + black</p>
    <p>back:<br>1 color<span class="spec__gap"></span>dark silver blue metallic</p>
    <p>on 8pt. card with matte varnish<br>3.5″ x 1.8″&nbsp;&nbsp; with radius cut corners</p>
  </div>

</main>
</body>
</html>
```